Kalvoria - a property developer - Website design

Hi all!
Exciting new project for you! :)
We are looking for some creative/modern designs to best represent us as a company.
Please have a look at the following link: huhu.kalvoria.example to get an idea about who we are and what we do.
The 'Main Page' of the HP should be neatly arranged, easy to navigate, contain several pictures (changing every 10 seconds or so) that should reflect that we are property developers.
The navigation points ('About us', 'Projects' 'Investment', 'Contact Us', 'Legal Notice') should be included in the Design (again under every navigation point, pictures may be added - that reflect our profession and/or the subsection)
What we will need at the end of the day is a fully functional site - i.e: a site that is designed and programmed with backend/wordpress, to allow us to make changes anytime we feel like it.
Further questions?! Don't hesitate to contact me! Thanks :)
Target Market(s)
Real Estate Development/Building sector
Industry/Entity Type
Real Estate Development
Number of Pages Required
5+ page
Look and feel

```html
<!DOCTYPE html>
<html lang="en">
<head>
<meta charset="utf-8">
<title>Kalvoria – Property Developer</title>
<link href="https://fonts.googleapis.com/css2?family=Oswald:wght@400;500&family=Roboto:wght@400;500&family=Ubuntu:wght@400;500;700&display=swap" rel="stylesheet">
<style>
:root{
  --teal:#4f96a0;
  --footer:#5b9fa7;
  --ice:#e9f9fc;
  --ink:#2b2b2b;
  --body:#555;
  --grey-band:#f1f1f1;
  --black:#151515;
  --white:#fff;
}
*{margin:0;padding:0;box-sizing:border-box}
html,body{width:1200px;height:2507px;overflow:hidden}
body{position:relative;background:var(--white);font-family:"Roboto",Arial,sans-serif;color:var(--body)}
.abs{position:absolute}
p.copy{font-size:12.5px;line-height:21px;color:var(--body)}
.nowrap{white-space:nowrap}

/* header */
.site-header{left:0;top:0;width:1200px;height:107px;background:var(--white)}
.brand{left:88px;top:30px;display:flex;align-items:center;gap:10px}
.brand .mark{width:20px;height:46px;background:#222}
.brand .name{font-family:"Ubuntu",sans-serif;font-weight:700;font-size:34px;letter-spacing:1px;color:#1d1d1d;line-height:1}
.brand .url{font-family:"Ubuntu",sans-serif;font-size:10px;color:#1d1d1d;margin-top:3px}
.main-nav{right:62px;top:38px;display:flex;align-items:center;gap:36px;font-size:13.5px;color:#555;text-transform:uppercase}
.main-nav .active{color:var(--teal)}
.lang{border:1px solid var(--teal);color:var(--teal);border-radius:6px;padding:7px 13px;font-size:11.5px}

/* hero */
.hero{left:0;top:107px;width:1200px;height:628px;background:linear-gradient(160deg,#7c7c7c 0%,#9b9b9b 40%,#8a8a8a 70%,#6f6f6f 100%)}
.hero-title{left:0;width:1200px;top:222px;line-height:60px;text-align:center;font-family:"Oswald",sans-serif;font-size:50px;color:#fff;letter-spacing:.5px;text-shadow:0 2px 4px rgba(0,0,0,.4)}
.hero-sub{left:0;width:1200px;top:288px;line-height:24px;text-align:center;font-size:20px;color:#fff;font-weight:500;text-shadow:0 1px 3px rgba(0,0,0,.4)}
.hero-btn{left:505px;top:344px;width:189px;height:50px;border:1.5px solid #eee;border-radius:4px;color:#fff;font-size:20px;display:flex;align-items:center;justify-content:center}
.slide-arrow{top:277px;width:34px;height:34px;border-radius:50%;background:#3a3a3a}
.slide-arrow svg{display:block}

/* welcome */
.welcome-title{left:0;width:1200px;top:778px;display:flex;justify-content:center;align-items:center;gap:12px;font-family:"Ubuntu",sans-serif;font-weight:500;font-size:29px;color:#222}
.welcome-title .mark{width:16px;height:32px;background:#222}
.welcome-title span.hl{color:var(--teal)}
.welcome-text{left:0;top:822px;width:1200px;text-align:center;font-size:12px !important;line-height:22px !important}

/* projects */
.projects{left:0;top:948px;width:1200px;height:498px;background:var(--ice);border-top:2px solid #d8eef2;border-bottom:2px solid #dfdfdf}
.section-title{left:0;width:1200px;text-align:center;font-family:"Ubuntu",sans-serif;font-weight:500;font-size:25px;color:var(--teal)}
.section-sub{left:0;width:1200px;text-align:center;font-size:16px;color:#444}
.card-photo{width:324px;height:201px;background:#fff;border:1px solid #ccc;padding:7px;box-shadow:0 1px 3px rgba(0,0,0,.15)}
.card-photo div{width:100%;height:100%}
.card-title{font-family:"Ubuntu",sans-serif;font-weight:500;font-size:17px;color:#222;text-transform:uppercase}
.card-text{font-size:11.5px;line-height:20px;white-space:nowrap}

/* about */
.about-photo{left:87px;top:1504px;width:431px;height:267px;background:#fff;border:1px solid #ccc;padding:7px;box-shadow:0 1px 4px rgba(0,0,0,.2)}
.about-photo div{width:100%;height:100%;background:linear-gradient(180deg,#3a63b8 0%,#6e8fd2 35%,#e8e8e8 55%,#cfcfcf 80%,#8a6a55 100%)}
.about-title{left:543px;top:1512px;font-family:"Ubuntu",sans-serif;font-weight:500;font-size:17.5px;color:var(--teal);text-transform:uppercase}
.about-text{left:543px;top:1543px;width:572px}
.read-more{left:541px;top:1736px;width:122px;height:35px;background:var(--teal);color:#fff;border-radius:3px;font-size:12px;font-weight:500;display:flex;align-items:center;justify-content:center;box-shadow:0 2px 2px rgba(0,0,0,.2)}

/* blog */
.blog{left:0;top:1822px;width:1200px;height:270px;background:var(--ice);border-top:2px solid #dfdfdf}
.blog-title{left:89px;top:1854px;font-family:"Ubuntu",sans-serif;font-weight:500;font-size:20px;color:#333}
.blog-title span{color:var(--teal)}
.blog-nav{left:1087px;top:1856px}
.post-photo{width:164px;height:137px;background:#fff;border:1px solid #ccc;padding:4px;box-shadow:0 1px 3px rgba(0,0,0,.2)}
.post-photo div{width:100%;height:100%}
.post-title{font-family:"Ubuntu",sans-serif;font-size:14.5px;color:#333}
.post-date{font-size:12.5px;color:#555}
.post-text{font-size:11.5px;line-height:20px;white-space:nowrap}

/* partners */
.partners{left:0;top:2092px;width:1200px;height:100px;background:var(--grey-band);border-top:1px solid #ddd}
.jv{left:88px;top:2122px;display:flex;gap:10px;align-items:center}
.jv .mark{width:16px;height:38px;background:#222}
.jv .txt{font-family:"Ubuntu",sans-serif;font-weight:500;font-size:16.5px;line-height:20px;color:var(--teal);text-transform:uppercase}
.partner{top:2128px;font-family:"Ubuntu",sans-serif;font-weight:500;font-size:18px;line-height:24px;color:#333}

/* footer */
.footer{left:0;top:2192px;width:1200px;height:214px;background:var(--footer);color:#fff}
.f-head{top:2226px;font-family:"Ubuntu",sans-serif;font-weight:500;font-size:13.5px;color:#fff;text-transform:uppercase}
.f-text{font-size:11.5px;line-height:20px;color:#f2f8f9}
.email-field{left:90px;top:2306px;width:212px;height:32px;background:#fff;border:1px solid #ccc;font-size:11px;color:#555;padding:9px 10px}
.subscribe{left:91px;top:2357px;width:96px;height:30px;background:#333;color:#fff;border-radius:3px;font-size:11.5px;display:flex;align-items:center;justify-content:center}
.tweet{left:394px;width:220px;display:flex;gap:8px}
.tweet .dot{width:10px;height:10px;border-radius:50%;background:#fff;margin-top:5px;flex:none}
.social{left:965px;display:flex;align-items:center;gap:14px}
.social .ring{width:36px;height:36px;border-radius:50%;border:1.5px solid #fff}
.bottom-bar{left:0;top:2406px;width:1200px;height:101px;background:var(--black);color:#fff;font-size:12.5px;display:flex;align-items:center;justify-content:center}
</style>
</head>
<body>

<header class="abs site-header">
  <div class="abs brand">
    <div class="mark"></div>
    <div>
      <div class="name">KALVORIA</div>
      <div class="url">huhu.kalvoria.example</div>
    </div>
  </div>
  <nav class="abs main-nav">
    <span class="active">Home</span>
    <span>About Us</span>
    <span>Projects</span>
    <span>Investment</span>
    <span>Contact Us</span>
    <span>Legal Notice</span>
    <span class="lang">English ▾</span>
  </nav>
</header>

<section class="abs hero" role="img" aria-label="Grey architectural wireframe rendering of a modern cubic house with balconies">
  <div class="abs hero-title">KALVORIA PROPERTY DEVELOPER</div>
  <div class="abs hero-sub">QUALITY, SKILLS AND EXPERIENCE: EVERYTHING UNDER ONE ROOF</div>
  <div class="abs hero-btn">VIEW MORE</div>
  <div class="abs slide-arrow" style="left:40px"><svg width="34" height="34"><path d="M19 11l-6 6 6 6" stroke="#fff" stroke-width="2" fill="none"/></svg></div>
  <div class="abs slide-arrow" style="left:1123px"><svg width="34" height="34"><path d="M15 11l6 6-6 6" stroke="#fff" stroke-width="2" fill="none"/></svg></div>
</section>

<h1 class="abs welcome-title"><span class="mark"></span>WELCOME TO <span class="hl">KALVORIA</span></h1>
<p class="abs copy welcome-text nowrap">Lorem Ipsum has been the industry's standard dummy text ever since the 1500s, when an unknown printer took a galley of type and scrambled it to make a type specimen<br>book. It has survived not only five centuries, but also the leap into electronic typesetting, remaining essentially unchanged. It was popularised in the 1960s with the release of<br>Lettrex sheets containing Lorem Ipsum passages, and more recently with desktop publishing software like Folio Layout including versions of Lorem Ipsum.</p>

<section class="abs projects"></section>
<h2 class="abs section-title" style="top:988px">OUR PROJECTS</h2>
<p class="abs section-sub" style="top:1034px">Lorem Ipsum is simply dummy text of the printing and typesetting industry</p>

<div class="abs card-photo" style="left:87px;top:1091px"><div role="img" aria-label="Photo of a white and ochre townhouse under blue sky" style="background:linear-gradient(180deg,#6f9bd6 0%,#a9c3e6 30%,#e7e4dc 55%,#c9a24a 80%,#5b6a3c 100%)"></div></div>
<div class="abs card-photo" style="left:438px;top:1091px"><div role="img" aria-label="Photo of a family house entrance with garage door" style="background:linear-gradient(180deg,#d9d9d9 0%,#bdbdbd 40%,#e9e9e9 65%,#7b8a6a 100%)"></div></div>
<div class="abs card-photo" style="left:789px;top:1091px"><div role="img" aria-label="Photo of a rooftop terrace with glass railing over the city" style="background:linear-gradient(180deg,#9db4cf 0%,#c6d1dc 35%,#8a8677 60%,#b86a3b 85%,#9a5a36 100%)"></div></div>

<h3 class="abs card-title" style="left:87px;top:1312px">Ardelweg - Townhouse</h3>
<h3 class="abs card-title" style="left:438px;top:1312px">Kornelgasse - Family House</h3>
<h3 class="abs card-title" style="left:789px;top:1312px">Brunnfeldgasse - Appartments</h3>
<p class="abs card-text" style="left:87px;top:1346px">Lorem Ipsum has been the industry's standard dummy text ever<br>since the 1500s, when an unknown printer took a galley of type</p>
<p class="abs card-text" style="left:438px;top:1346px">Lorem Ipsum has been the industry's standard dummy text ever<br>since the 1500s, when an unknown printer took a galley of type</p>
<p class="abs card-text" style="left:789px;top:1346px">Lorem Ipsum has been the industry's standard dummy text ever<br>since the 1500s, when an unknown printer took a galley of type</p>

<div class="abs about-photo"><div role="img" aria-label="Rendering of a white apartment building with planted balconies"></div></div>
<h2 class="abs about-title">Quality, skills and experience: everything under one roof.</h2>
<div class="abs about-text">
  <p class="copy">Lorem Ipsum has been the industry's standard dummy text ever since the 1500s, when an unknown printer took a galley of type and scrambled it to make a type specimen book. It has survived not only five centuries, but also the leap into electronic typesetting, remaining essentially unchanged. It was popularised in the 1960s with the release of Lettrex sheets containing</p>
  <p class="copy" style="margin-top:21px">&nbsp;It has survived not only five centuries, but also the leap into electronic typesetting, remaining essentially unchanged. It was popularised in the 1960s with the release of Lettrex sheets containing Lorem Ipsum passages, and more recently with desktop publishing software like Folio Layout</p>
</div>
<div class="abs read-more">READ MORE</div>

<section class="abs blog"></section>
<h2 class="abs blog-title">LATEST <span>BLOG</span></h2>
<svg class="abs blog-nav" width="26" height="20"><path d="M8 4l-6 6 6 6M18 4l6 6-6 6" stroke="#222" stroke-width="2" fill="none"/></svg>

<div class="abs post-photo" style="left:87px;top:1905px"><div role="img" aria-label="Photo of a modern house with wood cladding" style="background:linear-gradient(180deg,#7aa2d8 0%,#c8c3b2 45%,#b9874d 70%,#6b7a45 100%)"></div></div>
<div class="abs post-title" style="left:271px;top:1912px">Nemo Enim Ipsam Volup</div>
<div class="abs post-date" style="left:271px;top:1941px">09-07-2015</div>
<p class="abs post-text" style="left:271px;top:1967px">Lorem Ipsum has been the industry's standard dummy text<br>ever since the 1500s, when an unknown printer took a galley<br>of type and scrambled it to make a type specimen book.</p>

<div class="abs post-photo" style="left:622px;top:1902px"><div role="img" aria-label="Photo of a historic apartment building facade" style="background:linear-gradient(180deg,#c9c9c9 0%,#a07a5e 40%,#8a6650 70%,#5a5048 100%)"></div></div>
<div class="abs post-title" style="left:805px;top:1912px">Nemo Enim Ipsam Volup</div>
<div class="abs post-date" style="left:805px;top:1941px">09-07-2015</div>
<p class="abs post-text" style="left:805px;top:1967px">Lorem Ipsum has been the industry's standard dummy text<br>ever since the 1500s, when an unknown printer took a galley<br>of type and scrambled it to make a type specimen book.</p>

<section class="abs partners"></section>
<div class="abs jv"><div class="mark"></div><div class="txt">Kalvoria is a joint<br>venture between</div></div>
<div class="abs partner" style="left:375px">Morvane Group</div>
<div class="abs partner" style="left:610px">Delmor Holdings</div>
<div class="abs partner" style="left:850px">Tessaro Estates</div>

<footer class="abs footer"></footer>
<h4 class="abs f-head" style="left:90px">Newsletters Sign Up</h4>
<p class="abs f-text" style="left:90px;top:2256px;width:220px;line-height:16px;font-size:11px">Sign up for our daily email by entering your information below</p>
<div class="abs email-field">Email address</div>
<div class="abs subscribe">SUBSCRIBE</div>

<h4 class="abs f-head" style="left:394px">Latest Tweet</h4>
<div class="abs tweet" style="top:2262px"><span class="dot"></span><p class="f-text">Featured Workspace : Bluefoundry<br>lnk.example/8Rtw2Q 10 hours ago</p></div>
<div class="abs tweet" style="top:2314px"><span class="dot"></span><p class="f-text">Featured Workspace : Bluefoundry<br>lnk.example/8Rtw2Q 10 hours ago</p></div>

<h4 class="abs f-head" style="left:701px">Get in Touch</h4>
<p class="abs f-text" style="left:706px;top:2262px;line-height:25px">Address : Brennweg 7/TOP 4B<br>1220 Vienna - Austria<br>Phone: +43 1 555 0170<br>Fax: +43 1 555 0171<br>E-mail: info@kalvoria.example</p>

<h4 class="abs f-head" style="left:965px">Follow Us On</h4>
<div class="abs social" style="top:2265px"><span class="ring"></span><span class="f-text">Friendbook</span></div>
<div class="abs social" style="top:2308px"><span class="ring"></span><span class="f-text">Chirper</span></div>
<div class="abs social" style="top:2351px"><span class="ring"></span><span class="f-text">Snapgram</span></div>

<div class="abs bottom-bar">Copyright © 2015.. All Rights Reserved</div>

</body>
</html>
```